Stationary & Business Card design for Solo Law Firm
stationary and business card design
Stationary & Business Card design for Solo Law Firm - Law
Creative Brief
Professional
Mira Dalton
Attorney at Law
317 W. Halverd Street, Suite 508 Colorado Springs, CO 80903
miradalton@kestrelpointlegal.example
kestrelpointlegal.example
underneath my logo I want the following to appear Family Law - Business - Trust & Estates (the spacing or symbol between these terms is up to you)
Logo on the back with the wording above underneath
quillmarsh quillmarsh
#98 can you make the text on the front vertical? and use the back from your #95 with the blue background. I like your submission #72 as well.
#134 can you make the text on the front go vertically instead of horizontally? also can you make the scales on the back bigger?
#141 on the front can you make it vertical? and on the back can you make the logo bigger and put the scales on the back?

```html
<!DOCTYPE html>
<html lang="en">
<head>
<meta charset="utf-8">
<title>Kestrel Point Legal – Business Card</title>
<link href="https://fonts.googleapis.com/css2?family=Cormorant+Garamond:wght@500&display=swap" rel="stylesheet">
<style>
  :root {
    --backdrop: #d6d6d6;
    --rust: #c05a3b;
    --rust-deep: #a9492d;
    --rust-light: #cd6c4d;
    --paper: #ffffff;
    --stripe-blue: #2847a8;
    --stripe-red: #c9412f;
  }
  * { box-sizing: border-box; margin: 0; padding: 0; }
  html, body { width: 1200px; height: 908px; overflow: hidden; }
  body {
    background: var(--backdrop);
    position: relative;
    font-family: "Cormorant Garamond", Georgia, serif;
    font-weight: 500;
  }
  .card {
    position: absolute;
    top: 156px;
    width: 340px;
    height: 595px;
    border-radius: 22px;
    overflow: hidden;
    box-shadow: 0 10px 24px rgba(0,0,0,0.22);
  }
  .card--front { left: 220px; background: var(--rust); }
  .card--back { left: 640px; background: var(--paper); }

  /* landscape face turned to read upward */
  .face {
    position: absolute;
    width: 595px;
    height: 340px;
    left: -127.5px;
    top: 127.5px;
    transform: rotate(-90deg);
  }

  /* front */
  .front-face {
    background: linear-gradient(160deg, var(--rust-light), var(--rust) 55%, var(--rust-deep));
  }
  .decoration-area {
    position: absolute;
    right: 30px;
    top: 40px;
    width: 250px;
    height: 250px;
    border-radius: 50%;
    background: radial-gradient(circle, rgba(255,255,255,0.14), rgba(255,255,255,0) 70%);
  }
  .front-brand {
    position: absolute;
    left: 48px;
    bottom: 52px;
    color: var(--paper);
  }
  .brand-name {
    font-size: 34px;
    line-height: 1.1;
  }
  .practice-areas {
    margin-top: 12px;
    font-size: 15px;
    letter-spacing: 0.5px;
  }

  /* back */
  .back-face { background: var(--paper); }
  .back-brand {
    position: absolute;
    left: 40px;
    top: 135px;
    width: 230px;
    color: var(--rust);
  }
  .back-brand .brand-name { font-size: 28px; }
  .stripe {
    position: absolute;
    top: 0;
    bottom: 0;
    width: 3px;
  }
  .stripe--blue { left: 286px; background: var(--stripe-blue); }
  .stripe--red { left: 292px; background: var(--stripe-red); }
  .contact-panel {
    position: absolute;
    left: 295px;
    right: 0;
    top: 0;
    bottom: 0;
    background: var(--rust);
    color: var(--paper);
    padding: 44px 0 0 26px;
  }
  .contact-name { font-size: 19px; }
  .contact-title {
    font-size: 12px;
    letter-spacing: 1.5px;
    text-transform: uppercase;
    margin-bottom: 16px;
  }
  .contact-line { font-size: 12px; line-height: 1.45; }
</style>
</head>
<body>
  <section class="card card--front">
    <div class="face front-face">
      <div class="decoration-area" role="img" aria-label="Faint scales of justice decoration"></div>
      <div class="front-brand">
        <p class="brand-name">Kestrel Point Legal</p>
        <p class="practice-areas">Family Law · Business · Trust &amp; Estates</p>
      </div>
    </div>
  </section>

  <section class="card card--back">
    <div class="face back-face">
      <div class="back-brand">
        <p class="brand-name">Kestrel Point Legal</p>
      </div>
      <div class="stripe stripe--blue"></div>
      <div class="stripe stripe--red"></div>
      <div class="contact-panel">
        <p class="contact-name">Mira Dalton</p>
        <p class="contact-title">Attorney at Law</p>
        <p class="contact-line">317 W. Halverd Street, Suite 508</p>
        <p class="contact-line">Colorado Springs, CO 80903</p>
        <p class="contact-line">(719) 555-0142</p>
        <p class="contact-line">miradalton@kestrelpointlegal.example</p>
        <p class="contact-line">kestrelpointlegal.example</p>
      </div>
    </div>
  </section>
</body>
</html>
```